Business Card Design

Consultation for design, construction athletic facilities specializing in synthetic turf systems and all weather running track systems.
Motto "Independent Owner Advocacy"
New Company that we'd like to highlight the LOGO first and foremost with the colors of the background and font as primary colors of the card too if possible. I've also attached a typical larger project design layout that could be used in the background to highlight our design and construction specialty.
Website is something we want very noticeable for driving traffic.
Target Market(s)
Athletic Directors, Designers, Government and Military, Contractors
Industry/Entity Type
Construction
Contact Information for Business Card
Peter L. Vandrell CFB, CTB
48317 W 63rd Ave
Harlow Ridge, WA 99482
C +1 503.555.0147
O +1 808.555.0182
Peter@fieldlaneco.example
www.fieldlaneco.example

```html
<!DOCTYPE html>
<html lang="en">
<head>
<meta charset="utf-8">
<title>Halden Sport – Business Card</title>
<link rel="stylesheet" href="https://fonts.googleapis.com/css2?family=Open+Sans:wght@400;600;700&family=Tinos&display=swap">
<style>
  :root {
    --stage: #3a3431;
    --card-dark: #0b0a0a;
    --card-light: #fbfbfb;
    --ink-dark: #141414;
    --ink-light: #f2f2f2;
    --gold: #f0b400;
    --orange: #e2862a;
    --copper: #c77a4c;
    --grey-logo: #6d6d6d;
    --plan-dark: #1a1a1a;
    --plan-light: #ececec;
  }
  * { box-sizing: border-box; margin: 0; padding: 0; }
  html, body { width: 1200px; height: 768px; overflow: hidden; }
  body {
    background: var(--stage);
    font-family: "Open Sans", Arial, sans-serif;
    position: relative;
  }
  .card {
    position: absolute;
    top: 236px;
    width: 520px;
    height: 297px;
    overflow: hidden;
    box-shadow: 0 10px 24px rgba(0,0,0,.45);
  }
  .card--back { left: 50px; background: var(--card-dark); }
  .card--front { left: 630px; background: var(--card-light); }

  .site-plan { position: absolute; inset: 0; }
  .card--back .site-plan {
    background: radial-gradient(ellipse at 55% 45%, var(--plan-dark) 0%, var(--card-dark) 70%);
  }
  .card--front .site-plan {
    background: radial-gradient(ellipse at 65% 40%, var(--plan-light) 0%, var(--card-light) 70%);
  }

  .brand { position: absolute; text-align: center; white-space: nowrap; }
  .card--back .brand { left: 0; right: 0; top: 96px; }
  .card--front .brand { left: 50px; top: 66px; width: 260px; }

  .brand__name {
    display: inline-flex;
    align-items: center;
    gap: 12px;
    font-weight: 400;
    font-size: 30px;
    letter-spacing: 4px;
    text-transform: uppercase;
    white-space: nowrap;
  }
  .brand__dot { width: 14px; height: 14px; border-radius: 50%; flex: none; }
  .card--back .brand__name { color: var(--copper); }
  .card--back .brand__dot { background: var(--copper); }
  .card--front .brand__name { color: var(--grey-logo); font-size: 22px; letter-spacing: 3px; gap: 10px; }
  .card--front .brand__dot { background: var(--grey-logo); width: 10px; height: 10px; }

  .brand__motto {
    margin-top: 14px;
    font-family: "Tinos", "Times New Roman", serif;
    font-size: 15px;
  }
  .card--back .brand__motto { color: var(--ink-light); }
  .card--front .brand__motto { color: var(--ink-dark); font-size: 12px; margin-top: 10px; }

  .contact-band {
    position: absolute;
    left: 0; bottom: 0;
    width: 312px; height: 100px;
    background: var(--card-dark);
    color: var(--ink-light);
    padding: 18px 0 0 14px;
    font-size: 12px;
    line-height: 19px;
  }
  .contact-band__row { display: flex; align-items: center; gap: 8px; white-space: nowrap; }
  .contact-band__icon { width: 11px; height: 11px; flex: none; }

  .holder {
    position: absolute;
    right: 14px; top: 188px;
    text-align: right;
    color: var(--ink-dark);
    white-space: nowrap;
  }
  .holder__name { font-weight: 700; font-size: 15px; }
  .holder__title { font-size: 11px; margin-top: 2px; }

  .web-band {
    position: absolute;
    right: 0; bottom: 0;
    width: 208px; height: 56px;
    background: var(--gold);
    color: var(--ink-dark);
    font-size: 13px;
    font-weight: 600;
    display: flex;
    align-items: center;
    justify-content: center;
    white-space: nowrap;
  }
</style>
</head>
<body>

<section class="card card--back" aria-label="Card back">
  <div class="site-plan" role="img" aria-label="Faint athletic facility site plan with running track outline"></div>
  <div class="brand">
    <div class="brand__name"><span class="brand__dot"></span>Halden Sport</div>
    <p class="brand__motto">Independent Owner Advocacy</p>
  </div>
</section>

<section class="card card--front" aria-label="Card front">
  <div class="site-plan" role="img" aria-label="Faint athletic facility site plan with running track outline"></div>
  <div class="brand">
    <div class="brand__name"><span class="brand__dot"></span>Halden Sport</div>
    <p class="brand__motto">Independent Owner Advocacy</p>
  </div>

  <div class="holder">
    <p class="holder__name">Peter L. Vandrell</p>
    <p class="holder__title">CFB, CTB</p>
  </div>

  <div class="contact-band">
    <p class="contact-band__row">
      <svg class="contact-band__icon" viewBox="0 0 12 12" aria-hidden="true"><path d="M6 0.5a4 4 0 0 0-4 4c0 3 4 7 4 7s4-4 4-7a4 4 0 0 0-4-4z" fill="var(--orange)"/><circle cx="6" cy="4.5" r="1.5" fill="var(--card-dark)"/></svg>
      48317 W 63rd Ave Harlow Ridge, WA 99482
    </p>
    <p class="contact-band__row">
      <svg class="contact-band__icon" viewBox="0 0 12 12" aria-hidden="true"><path d="M2.5 1l2 2.2-1 1.3c.7 1.5 1.8 2.6 3.2 3.3l1.3-1 2.2 2-1 1.7C5 10 1.8 6.6 1 2.2z" fill="var(--orange)"/></svg>
      +1 503.555.0147 &nbsp;(O) +1 808.555.0182
    </p>
    <p class="contact-band__row">
      <svg class="contact-band__icon" viewBox="0 0 12 12" aria-hidden="true"><rect x="0.5" y="2" width="11" height="8" fill="var(--orange)"/><path d="M0.5 2l5.5 4.5L11.5 2" fill="none" stroke="var(--card-dark)" stroke-width="1"/></svg>
      Peter@fieldlaneco.example
    </p>
  </div>

  <div class="web-band">www.fieldlaneco.example</div>
</section>

</body>
</html>
```